Need Business Card for our Real Estate Business with Sales Executive's Picture

PANTONE 484 C ( RED)

PANTONE 2766 C ( BLUE

Industry/Entity Type

Real Estate

Contact Information for Business Card

Name, Mobile, email, & picture of Person
Agency Phone, address, Web address

Requirements
Must have
• Our Logo Colours, Agent Picture,

```html
<!DOCTYPE html>
<html lang="en">
<head>
<meta charset="utf-8">
<title>Meridian Realty – Business Card</title>
<link rel="stylesheet" href="https://fonts.googleapis.com/css2?family=Tinos:wght@400;700&display=swap">
<style>
  :root {
    --backdrop: #8a8a8a;
    --navy: #0f1a4b;
    --navy-deep: #0b1540;
    --maroon: #8b1e26;
    --white: #ffffff;
    --photo-light: #c9cde0;
    --photo-dark: #2a3a8a;
  }
  html, body {
    margin: 0;
    padding: 0;
    width: 1200px;
    height: 1200px;
    overflow: hidden;
    background: var(--backdrop);
  }
  .canvas {
    position: relative;
    width: 1200px;
    height: 1200px;
    display: flex;
    align-items: center;
    justify-content: center;
    gap: 36px;
  }
  .card {
    width: 540px;
    height: 325px;
    display: block;
    box-shadow: 0 4px 14px rgba(0,0,0,0.35);
  }
  .serif { font-family: 'Tinos', 'Times New Roman', serif; }
  .brand-name { font-weight: 400; fill: var(--navy); letter-spacing: 1.5px; }
  .brand-name--light { fill: var(--white); }
  .agent-name { font-weight: 700; fill: var(--navy); }
  .agent-role { font-weight: 700; fill: var(--white); }
  .contact-line { font-weight: 700; fill: var(--white); }
  .web-address { font-weight: 400; fill: var(--white); }
</style>
</head>
<body>
<main class="canvas">

  <!-- Front of card -->
  <svg class="card card--front" viewBox="0 0 448 270" xmlns="http://www.w3.org/2000/svg">
    <defs>
      <linearGradient id="photoTone" x1="0" y1="0" x2="0" y2="1">
        <stop offset="0" stop-color="var(--photo-light)"/>
        <stop offset="1" stop-color="var(--photo-dark)"/>
      </linearGradient>
    </defs>
    <rect class="card-base" width="448" height="270" fill="var(--white)"/>

    <!-- navy diagonal panel -->
    <polygon class="panel" points="340,0 448,0 448,270 150,270 150,252 214,252" fill="var(--navy)"/>
    <!-- accent stripes -->
    <polyline class="stripe stripe--maroon" points="320,0 196,238 128,238" fill="none" stroke="var(--maroon)" stroke-width="4"/>
    <polyline class="stripe stripe--navy" points="331,0 205,245 138,245" fill="none" stroke="var(--navy)" stroke-width="2.5"/>

    <!-- agent portrait area -->
    <rect class="agent-photo" x="0" y="108" width="135" height="162" fill="url(#photoTone)" role="img" aria-label="Portrait photo of the agent"/>

    <!-- brand -->
    <rect class="brand-mark" x="20" y="60" width="8" height="8" fill="var(--maroon)"/>
    <text class="serif brand-name" x="34" y="68" font-size="14">MERIDIAN</text>
    <text class="serif brand-name" x="34" y="82" font-size="9">REALTY</text>

    <!-- name banner -->
    <polygon class="name-banner" points="292,36 448,36 448,63 278,63" fill="var(--white)"/>
    <line x1="276" y1="67" x2="448" y2="67" stroke="var(--white)" stroke-width="1.5"/>
    <text class="serif agent-name" x="428" y="57" font-size="18" text-anchor="end">Alex Morgan</text>
    <text class="serif agent-role" x="428" y="81" font-size="11" text-anchor="end">Agent</text>

    <!-- contact lines -->
    <g class="contact-list">
      <g class="contact-item">
        <text class="serif contact-line" x="404" y="112" font-size="9.5" text-anchor="end">555-014-2200</text>
        <polygon points="419,100 427,104.5 427,113.5 419,118 411,113.5 411,104.5" fill="var(--white)" stroke="var(--maroon)" stroke-width="1"/>
        <rect x="416.5" y="104" width="5" height="9" rx="1" fill="none" stroke="var(--maroon)" stroke-width="1"/>
      </g>
      <g class="contact-item">
        <text class="serif contact-line" x="404" y="144" font-size="9.5" text-anchor="end">alex@meridianrealty.co.uk</text>
        <polygon points="419,132 427,136.5 427,145.5 419,150 411,145.5 411,136.5" fill="var(--white)" stroke="var(--maroon)" stroke-width="1"/>
        <rect x="414.5" y="138" width="9" height="6" fill="none" stroke="var(--maroon)" stroke-width="1"/>
        <polyline points="414.5,138 419,141.5 423.5,138" fill="none" stroke="var(--maroon)" stroke-width="1"/>
      </g>
      <g class="contact-item">
        <text class="serif contact-line" x="404" y="177" font-size="9.5" text-anchor="end">555-018 3321</text>
        <polygon points="419,165 427,169.5 427,178.5 419,183 411,178.5 411,169.5" fill="var(--white)" stroke="var(--maroon)" stroke-width="1"/>
        <path d="M415.5,170 q0,6 7,9 l1-2 -2-1.5 -1,1 q-2.5-1 -3.5-3.5 l1-1 -1.5-2z" fill="none" stroke="var(--maroon)" stroke-width="1"/>
      </g>
      <g class="contact-item">
        <text class="serif contact-line" x="404" y="209" font-size="9.5" text-anchor="end">418 Bayview Rd, Fairport, FL 32500</text>
        <polygon points="419,197 427,201.5 427,210.5 419,215 411,210.5 411,201.5" fill="var(--white)" stroke="var(--maroon)" stroke-width="1"/>
        <path d="M419,212 l-3.5-5 a3.5,3.5 0 1,1 7,0 z" fill="none" stroke="var(--maroon)" stroke-width="1"/>
        <circle cx="419" cy="205.5" r="1" fill="var(--maroon)"/>
      </g>
      <g class="contact-item">
        <text class="serif contact-line" x="404" y="242" font-size="9.5" text-anchor="end">www.meridianrealty.co.uk</text>
        <polygon points="419,230 427,234.5 427,243.5 419,248 411,243.5 411,234.5" fill="var(--white)" stroke="var(--maroon)" stroke-width="1"/>
        <circle cx="419" cy="239" r="4.5" fill="none" stroke="var(--maroon)" stroke-width="1"/>
        <ellipse cx="419" cy="239" rx="2" ry="4.5" fill="none" stroke="var(--maroon)" stroke-width="0.8"/>
        <line x1="414.5" y1="239" x2="423.5" y2="239" stroke="var(--maroon)" stroke-width="0.8"/>
      </g>
    </g>
  </svg>

  <!-- Back of card -->
  <svg class="card card--back" viewBox="0 0 448 270" xmlns="http://www.w3.org/2000/svg">
    <rect class="card-base" width="448" height="270" fill="var(--navy-deep)"/>
    <rect class="brand-mark" x="141" y="134" width="10" height="10" fill="var(--maroon)"/>
    <text class="serif brand-name brand-name--light" x="232" y="145" font-size="24" text-anchor="middle">MERIDIAN</text>
    <text class="serif brand-name brand-name--light" x="224" y="162" font-size="9" text-anchor="middle">REALTY</text>
    <text class="serif web-address" x="224" y="233" font-size="11" text-anchor="middle">www.meridianrealty.co.uk</text>
  </svg>

</main>
</body>
</html>
```